Brisk Hollow Builders Needs A Flyer

We need a flyer for our newest product "The Cedarlane Garden Workroom"

Here is some copy for the flyer:

1. More and more people everyday are working from home and finding it difficult to disconnect from home activities in order to focus on their work. They are also finding it very expensive to add on to their existing house for a quiet place. Our archatectually stunning, Cedarlane Garden Workroom is the answer. The office studio measures 16' wide and 10' deep. 160 Square feet of space.

Perfect for dozens of purposes. Home office, design studio, artist studio, home school office, reading room, craft studio, drafting room.

Features include:

- Steel Framing. 40-60% lighter then wood, higher strength to weight ratio, resistant to mold and fire and steel is the most recycled material on earth!
- Spray foam insulation. Cool in the summer and warm in the winter.
- HVAC Mini Split with wireless remote control and thermostat.
- 100% Off grid with enough solar and battery storage to run your entire office. No need to pay for an expensive electric installation.
- Flush fitting floor outlets to reduce wires.
- TV mount (Optional with pre-wired electric, HDMI, digital audio & Cat 6)
- Windows are tempered glass custom made by Morvik Glazing.
- Solar qualifies for a 26% tax credit. This is not a write-off rather it is a direct reduction on your tax obligation.
- Thousands of dollars less than adding onto your home.
- Custom color, siding, features available.

This beautiful back yard office is delivered 100% assembled and ready to enjoy on the day of delivery.

We ship nationwide from our factory in South Carolina. Give us a call anytime to speak to a designer and start your dream office today!

555-318-4027
info@BriskHollowBuilders.example

```html
<!DOCTYPE html>
<html lang="en">
<head>
<meta charset="utf-8">
<title>Brisk Hollow Builders – The Cedarlane Garden Workroom</title>
<link rel="stylesheet" href="https://fonts.googleapis.com/css2?family=Oswald:wght@500;600&family=Courgette&family=Source+Sans+3:wght@400;600;700&display=swap">
<style>
  :root {
    --green: #4f9b2f;
    --green-light: #72b740;
    --green-dark: #1f3a1c;
    --orange: #f6a91f;
    --orange-deep: #ef8f12;
    --ink: #333333;
    --white: #ffffff;
  }
  * { margin: 0; padding: 0; box-sizing: border-box; }
  html, body { width: 800px; height: 1200px; overflow: hidden; background: var(--white); }
  .flyer { position: relative; width: 800px; height: 1200px; overflow: hidden; font-family: "Source Sans 3", Arial, sans-serif; color: var(--ink); }
  .backdrop { position: absolute; inset: 0; }

  .brand { position: absolute; left: 30px; top: 70px; width: 240px; display: flex; align-items: center; gap: 10px; }
  .brand-dot { width: 34px; height: 34px; border-radius: 50%; background: var(--green); flex: none; }
  .brand-name { font-family: "Oswald", sans-serif; font-weight: 600; font-size: 27px; line-height: 1.05; color: var(--green); text-transform: uppercase; }

  .headline { position: absolute; left: 33px; top: 252px; font-family: "Oswald", sans-serif; font-weight: 500; font-size: 37px; line-height: 1.38; color: var(--white); text-transform: uppercase; letter-spacing: 0.2px; }

  .tagline { position: absolute; left: 33px; top: 602px; font-family: "Courgette", cursive; font-weight: 400; font-size: 22px; line-height: 32px; color: var(--green); white-space: nowrap; }
  .uses { position: absolute; left: 33px; top: 641px; font-family: "Oswald", sans-serif; font-weight: 500; font-size: 13.5px; line-height: 26px; color: var(--orange-deep); text-transform: uppercase; white-space: nowrap; }
  .body-copy { position: absolute; left: 33px; top: 708px; width: 415px; font-size: 12.6px; line-height: 16px; }
  .body-copy p { margin-bottom: 23px; }

  .delivery { position: absolute; left: 33px; top: 896px; width: 405px; text-align: center; font-family: "Oswald", sans-serif; font-weight: 500; font-size: 13px; line-height: 19px; color: var(--green); text-transform: uppercase; }

  .gallery { position: absolute; left: 38px; top: 948px; display: flex; gap: 10px; }
  .gallery-item { width: 124px; height: 92px; background: linear-gradient(180deg, #3d3d3d 0%, #5a5a55 35%, #c9b79a 70%, #3a3a38 100%); border-top: 6px solid #2b2b2b; }

  .features { position: absolute; left: 460px; top: 600px; width: 320px; height: 438px; background: var(--green); border-radius: 0 0 34px 34px; padding: 54px 16px 0 16px; }
  .features-tab { position: absolute; left: -12px; top: 0; width: 232px; height: 38px; background: var(--orange); border-radius: 0 19px 19px 0; font-family: "Source Sans 3", sans-serif; font-weight: 700; font-size: 16px; color: var(--white); padding: 9px 0 0 26px; text-transform: uppercase; }
  .feature-list { list-style: none; }
  .feature-list li { position: relative; padding: 0 0 6px 16px; margin-bottom: 6px; font-size: 11px; line-height: 1.12; color: var(--white); border-bottom: 1px dotted rgba(255,255,255,0.55); }
  .feature-list li:last-child { border-bottom: none; }
  .feature-list li::before { content: ""; position: absolute; left: 1px; top: 2px; width: 8px; height: 8px; border-radius: 50%; border: 2px solid var(--orange); background: var(--white); }

  .shipping { position: absolute; left: 520px; top: 1062px; width: 270px; font-size: 11px; line-height: 1.3; color: var(--orange-deep); }

  .contact { position: absolute; left: 36px; top: 1132px; font-size: 19px; font-weight: 600; color: var(--white); line-height: 1.5; }
  .contact-line { display: flex; align-items: center; gap: 10px; }
  .contact-line svg { width: 16px; height: 16px; flex: none; }
  .phone { position: absolute; left: 522px; top: 1150px; display: flex; align-items: center; gap: 10px; font-size: 31px; font-weight: 600; color: var(--white); }
  .phone svg { width: 28px; height: 28px; }
</style>
</head>
<body>
<main class="flyer">
  <svg class="backdrop" width="800" height="1200" viewBox="0 0 800 1200">
    <defs>
      <linearGradient id="sceneTone" x1="0" y1="0" x2="0" y2="1">
        <stop offset="0" stop-color="#9cc7e6"/>
        <stop offset="0.3" stop-color="#5c7a4a"/>
        <stop offset="0.6" stop-color="#3a3c36"/>
        <stop offset="1" stop-color="#6f8f55"/>
      </linearGradient>
      <linearGradient id="gardenTone" x1="0" y1="0" x2="1" y2="1">
        <stop offset="0" stop-color="#203b1d"/>
        <stop offset="1" stop-color="#35562c"/>
      </linearGradient>
      <linearGradient id="circleExterior" x1="0" y1="0" x2="0" y2="1">
        <stop offset="0" stop-color="#b9d3e6"/>
        <stop offset="0.45" stop-color="#5a5a55"/>
        <stop offset="1" stop-color="#6a8c4a"/>
      </linearGradient>
    </defs>

    <rect x="0" y="0" width="800" height="610" fill="url(#gardenTone)" role="img" aria-label="Garden foliage behind the headline"/>
    <path d="M330 0 H800 V470 C700 555 560 572 420 555 C380 550 350 548 330 546 Z" fill="url(#sceneTone)" role="img" aria-label="Photo of the garden workroom with glass doors and a stone path"/>

    <path d="M0 0 H440 C380 70 330 205 170 222 C100 230 40 222 0 232 Z" fill="var(--green)"/>
    <path d="M0 0 H420 C360 60 320 192 160 205 C90 212 30 206 0 215 Z" fill="var(--white)"/>

    <path d="M0 555 C150 518 300 535 420 552 C560 575 700 555 800 462 V1200 H0 Z" fill="var(--green-light)"/>
    <path d="M0 578 C150 545 300 555 420 572 C560 595 700 575 800 495 V1200 H0 Z" fill="var(--green)"/>
    <path d="M0 596 C150 566 300 572 420 588 C560 608 700 590 800 522 V1200 H0 Z" fill="var(--white)"/>

    <circle cx="108" cy="490" r="86" fill="url(#circleExterior)" stroke="var(--orange)" stroke-width="5" role="img" aria-label="Exterior view of the workroom with solar roof"/>
    <circle cx="260" cy="496" r="76" fill="#e9e9e9" stroke="var(--orange)" stroke-width="5" role="img" aria-label="Line drawing of the workroom frame"/>

    <path d="M0 1075 C180 1048 360 1058 450 1090 C560 1128 700 1120 800 1085 V1105 C700 1140 560 1145 450 1110 C360 1080 180 1070 0 1092 Z" fill="var(--orange)"/>
    <path d="M0 1092 C180 1070 360 1080 450 1110 C560 1145 700 1140 800 1105 V1200 H0 Z" fill="var(--green)"/>

    <g>
      <path d="M445 1135 L432 1165 L468 1142 Z" fill="var(--orange)"/>
      <circle cx="470" cy="1098" r="46" fill="var(--orange)"/>
      <rect x="444" y="1082" width="34" height="26" rx="3" fill="var(--white)"/>
      <path d="M480 1090 H492 L500 1100 V1108 H480 Z" fill="var(--white)"/>
      <circle cx="454" cy="1111" r="5" fill="var(--white)" stroke="var(--orange)" stroke-width="2"/>
      <circle cx="490" cy="1111" r="5" fill="var(--white)" stroke="var(--orange)" stroke-width="2"/>
    </g>
  </svg>

  <div class="brand">
    <span class="brand-dot"></span>
    <span class="brand-name">Brisk Hollow<br>Builders</span>
  </div>

  <h1 class="headline">The Cedarlane<br>Garden Workroom</h1>

  <h2 class="tagline">Perfect for dozens of purposes.</h2>
  <p class="uses">Home office, design studio, artist studio,<br>home school office, reading room, craft studio, drafting room.</p>
  <div class="body-copy">
    <p>More and more people everyday are working from home and finding it difficult to disconnect from home activities in order to focus on their work.</p>
    <p>They are also finding it very expensive to add on to their existing house for a quiet place.</p>
    <p>Our archatectually stunning, Cedarlane Garden Workroom is the answer.<br>The office studio measures 16' wide and 10' deep.<br>160 Square feet of space.</p>
  </div>

  <p class="delivery">This beautiful back yard office is delivered 100% assembled<br>and ready to enjoy on the day of delivery.</p>

  <div class="gallery">
    <div class="gallery-item" role="img" aria-label="Workroom exterior, angled view"></div>
    <div class="gallery-item" role="img" aria-label="Workroom exterior, front view"></div>
    <div class="gallery-item" role="img" aria-label="Workroom exterior, opposite angle"></div>
  </div>

  <section class="features">
    <h3 class="features-tab">Features include:</h3>
    <ul class="feature-list">
      <li>Steel Framing. 40-60% lighter then wood, higher strength to weight ratio, resistant to mold and fire and steel is the most recycled material on earth!</li>
      <li>Spray foam insulation. Cool in the summer and warm in the winter.</li>
      <li>HVAC Mini Split with wireless remote control and thermostat.</li>
      <li>100% Off grid with enough solar and battery storage to run your entire office. No need to pay for an expensive electric installation.</li>
      <li>Flush fitting floor outlets to reduce wires.</li>
      <li>TV mount (Optional with pre-wired electric, HDMI, digital audio &amp; Cat 6)</li>
      <li>Windows are tempered glass custom made by Morvik Glazing.</li>
      <li>Solar qualifies for a 26% tax credit. This is not a write-off rather it is a direct reduction on your tax obligation.</li>
      <li>Thousands of dollars less than adding onto your home.</li>
      <li>Custom color, siding, features available.</li>
    </ul>
  </section>

  <p class="shipping">We ship nationwide from our factory in South Carolina.<br>Give us a call anytime to speak to a designer and start<br>your dream office today!</p>

  <div class="contact">
    <div class="contact-line">
      <svg viewBox="0 0 16 16" aria-hidden="true"><circle cx="8" cy="8" r="7" fill="none" stroke="#fff" stroke-width="1.5"/><path d="M1 8 H15 M8 1 C4 5 4 11 8 15 M8 1 C12 5 12 11 8 15" fill="none" stroke="#fff" stroke-width="1.2"/></svg>
      <span>www.BriskHollowBuilders.example</span>
    </div>
    <div class="contact-line">
      <svg viewBox="0 0 16 16" aria-hidden="true"><circle cx="8" cy="8" r="7.5" fill="#fff"/><rect x="4" y="5" width="8" height="6" fill="none" stroke="#4f9b2f" stroke-width="1.2"/><path d="M4 5 L8 8.5 L12 5" fill="none" stroke="#4f9b2f" stroke-width="1.2"/></svg>
      <span>info@BriskHollowBuilders.example</span>
    </div>
  </div>

  <div class="phone">
    <svg viewBox="0 0 28 28" aria-hidden="true"><circle cx="14" cy="14" r="12.5" fill="none" stroke="#fff" stroke-width="2"/><path d="M9 8 C9 15 13 19 20 20 L21 17 L18 15.5 L16.5 17 C14 16 12 14 11 11.5 L12.5 10 L11 7 Z" fill="#fff"/></svg>
    <span>555-318-4027</span>
  </div>
</main>
</body>
</html>
```